Business Card Design

We are a flooring/granite/cabinet company
want a sleek and modern design card. Will send our logo. maybe our logo in 3d on card.
black card

Industry/Entity Type

Business

Contact Information for Business Card

Gregory Tallis
company name Stone Hearth Depot
4827 fm 71s 78540
210-634-8872
stonehearthdepot@mailvista.example

```html
<!DOCTYPE html>
<html lang="en">
<head>
<meta charset="utf-8">
<title>Stone Hearth Depot – Business Card</title>
<link rel="stylesheet" href="https://fonts.googleapis.com/css2?family=Cinzel:wght@400;700&display=swap">
<style>
  :root {
    --page: #ffffff;
    --card-light: #2c2d2f;
    --card-dark: #0f1011;
    --band: #4f7fb2;
    --band-light: #5a8abd;
    --brand: #1f4f78;
    --name-light: #cfe6f5;
    --name-dark: #6fa6c9;
    --contact-ink: #15171b;
  }
  * { margin: 0; padding: 0; box-sizing: border-box; }
  html, body {
    width: 1200px; height: 1000px; overflow: hidden;
    background: var(--page);
    font-family: "Cinzel", serif;
  }
  .canvas { position: relative; width: 1200px; height: 1000px; }
  .card { position: absolute; overflow: hidden; }
  .card-front { left: 0; top: 0; width: 868px; height: 496px; }
  .card-back { left: 330px; top: 503px; width: 870px; height: 497px; }
  .card-art { position: absolute; inset: 0; width: 100%; height: 100%; }

  .brand-name {
    position: absolute; left: 300px; top: 232px; width: 560px;
    text-align: center;
    font-family: "Cinzel", serif; font-weight: 700; font-size: 40px;
    letter-spacing: 2px; color: var(--brand);
  }

  .person-name {
    position: absolute; right: 42px; top: 98px;
    font-family: "Cinzel", serif; font-weight: 400; font-size: 58px;
    letter-spacing: 1px; line-height: 1;
    background: linear-gradient(180deg, var(--name-light), var(--name-dark));
    -webkit-background-clip: text; background-clip: text; color: transparent;
    filter: drop-shadow(3px 4px 3px rgba(0,0,0,0.8));
  }

  .contact {
    position: absolute; display: flex; align-items: center; gap: 14px;
    font-family: "Cinzel", serif; color: var(--contact-ink);
    font-size: 20px; line-height: 1;
  }
  .contact svg { flex: none; }
  .contact-email { left: 377px; top: 303px; font-size: 17px; }
  .contact-phone { left: 418px; top: 355px; }
  .contact-address { left: 454px; top: 412px; }
</style>
</head>
<body>
<main class="canvas">

  <section class="card card-front" aria-label="Card front">
    <svg class="card-art" viewBox="0 0 868 496" aria-hidden="true">
      <defs>
        <radialGradient id="frontBg" cx="0.6" cy="0.35" r="0.8">
          <stop offset="0" stop-color="var(--card-light)"/>
          <stop offset="1" stop-color="var(--card-dark)"/>
        </radialGradient>
        <linearGradient id="frontBand" x1="0" y1="0" x2="1" y2="1">
          <stop offset="0" stop-color="var(--band-light)"/>
          <stop offset="1" stop-color="var(--band)"/>
        </linearGradient>
      </defs>
      <rect width="868" height="496" fill="url(#frontBg)"/>
      <polygon points="0,0 155,0 462,496 205,496 0,175" fill="url(#frontBand)"/>
    </svg>
    <p class="brand-name">STONE HEARTH DEPOT</p>
  </section>

  <section class="card card-back" aria-label="Card back">
    <svg class="card-art" viewBox="0 0 870 497" aria-hidden="true">
      <defs>
        <radialGradient id="backBg" cx="0.65" cy="0.3" r="0.8">
          <stop offset="0" stop-color="var(--card-light)"/>
          <stop offset="1" stop-color="var(--card-dark)"/>
        </radialGradient>
        <linearGradient id="backBand" x1="0" y1="0" x2="1" y2="1">
          <stop offset="0" stop-color="var(--band-light)"/>
          <stop offset="1" stop-color="var(--band)"/>
        </linearGradient>
      </defs>
      <rect width="870" height="497" fill="url(#backBg)"/>
      <polygon points="0,0 160,0 465,497 210,497 0,165" fill="url(#backBand)"/>
      <g class="contact-bars" fill="var(--band)">
        <polygon points="340,297 870,297 870,330 360,330"/>
        <polygon points="395,352 870,352 870,385 415,385"/>
        <polygon points="445,410 870,410 870,443 465,443"/>
      </g>
    </svg>

    <h1 class="person-name">GREGORY TALLIS</h1>

    <p class="contact contact-email">
      <svg width="26" height="18" viewBox="0 0 26 18" aria-hidden="true">
        <rect x="1" y="1" width="24" height="16" fill="#111"/>
        <polyline points="1,1 13,10 25,1" fill="none" stroke="#4f7fb2" stroke-width="1.5"/>
      </svg>
      stonehearthdepot@mailvista.example
    </p>
    <p class="contact contact-phone">
      <svg width="22" height="28" viewBox="0 0 22 28" aria-hidden="true">
        <path d="M5 1 L9 7 L6 10 C7 15 10 19 14 21 L17 18 L21 23 L17 27 C8 25 2 15 1 5 Z" fill="#111"/>
      </svg>
      210-634-8872
    </p>
    <p class="contact contact-address">
      <svg width="20" height="28" viewBox="0 0 20 28" aria-hidden="true">
        <path d="M10 1 C4 1 1 5 1 10 C1 17 10 27 10 27 C10 27 19 17 19 10 C19 5 16 1 10 1 Z" fill="#111"/>
        <circle cx="10" cy="10" r="3.5" fill="#4f7fb2"/>
      </svg>
      4827 FM 71S 78540
    </p>
  </section>

</main>
</body>
</html>
```